We need banner ads in different sizes for a boat sales event on Grand Lake, OK. People will need to go to 5 different locations and they have the option if they go to all the stops of winning a $2000 tropical travel voucher. Most of the boats are 30' yachts such as WaveKite, Corvant, Helmstrand, Dolan Marsh brands plus jet ski.

Please do not use more than 7 elements.
Name - Tide and Tally Dockside Boat Fair
April 29-May 1st
Grand Lake, Oklahoma
Over 100 new and pre-owned boats at 5 locations and 7 boat dealers

Standard Ad Unit Sizes – W X H
Inline Rectangle
300 X 250
Leaderboard
728 X 90
Large Rectangle
336 X 280
Wide Skyscraper
160 X 600
Banner
468 X 60
Skyscraper
120 X 600
Square
250 X 250
Small Square
200 X 200

· Maximum file size is 150KB for each ad.

· Acceptable file types for non-animated ads: .jpg (my preferred), .png and .gif

Target Market(s)

Men in their 30-50 Range

Industry/Entity Type

Event

Font styles to use
Serif

Colors
0255a3
85cae6
33b8a4

Requirements
Must have
• Logo, Date, Boat or nautical element and win a tropical travel voucher
Nice to have
• Map of locations
Should not have
• Does not need to have website on the ad

```html
<!DOCTYPE html>
<html lang="en">
<head>
<meta charset="utf-8">
<title>Tide and Tally Dockside Boat Fair – Banner Set</title>
<link href="https://fonts.googleapis.com/css2?family=Montserrat:wght@600;700;800&family=Roboto:wght@400;500;700&display=swap" rel="stylesheet">
<style>
:root{
  --board:#252624;
  --label:#8a8b88;
  --teal:#33a9b8;
  --teal-deep:#2a97a6;
  --sky:#85cae6;
  --ice:#d3edf5;
  --navy:#1b2238;
  --white:#ffffff;
  --sea-a:#1d4f80;
  --sea-b:#5f94bd;
  --sand-a:#f3c9a1;
  --sand-b:#b98a74;
}
*{box-sizing:border-box;margin:0;padding:0}
html,body{width:1200px;height:1200px;overflow:hidden;background:var(--board)}
.board{position:relative;width:1200px;height:1200px;font-family:"Montserrat",sans-serif}
.size-label{position:absolute;color:var(--label);font:700 15px "Montserrat",sans-serif;letter-spacing:.5px;transform:translate(-50%,-50%);white-space:nowrap}
.ad{position:absolute;background:var(--white);overflow:hidden;color:var(--navy)}
.photo{position:absolute;left:0;top:0}
.photo.sea{background:linear-gradient(160deg,var(--sea-a),var(--sea-b) 60%,#9fc0d8)}
.photo.sunset{background:linear-gradient(170deg,var(--sand-a),#e6b08c 55%,var(--sand-b))}
.photo.lake{background:linear-gradient(180deg,#c9d9e8 0%,#7aa3c4 35%,#4d7ea6 70%,#8db3cf 100%)}
.wave{position:absolute;left:0;width:100%}
.t{color:var(--teal)}
.logo{position:absolute;display:flex;flex-direction:column;align-items:center;justify-content:center;gap:2px}
.logo-dot{border-radius:50%;border:1.5px solid var(--teal)}
.logo-name{font-family:"Montserrat",sans-serif;font-weight:700;color:var(--teal);white-space:nowrap;letter-spacing:.3px}

/* skyscraper */
.sky{left:187px;top:185px;width:96px;height:480px;text-align:center}
.sky .photo{width:96px;height:150px}
.sky .wave{top:118px;height:40px}
.sky .logo{left:0;width:96px;top:158px;height:60px}
.sky .logo-dot{width:24px;height:24px}
.sky .logo-name{font-size:7.5px}
.sky-date{position:absolute;left:16px;width:64px;top:219px;height:28px;border-left:1px solid var(--navy);border-right:1px solid var(--navy);font:700 11px/14px "Montserrat",sans-serif}
.sky-head{position:absolute;left:0;width:96px;top:266px;font:700 11.5px/14.5px "Montserrat",sans-serif}
.sky-rule{position:absolute;left:30px;width:36px;top:333px;border-top:1.5px solid var(--teal)}
.sky-voucher{position:absolute;left:0;width:96px;top:341px;height:38px;background:var(--ice);font:800 6px/7.8px "Montserrat",sans-serif;padding-top:4px}
.sky-loc{position:absolute;left:0;width:96px;top:383px;font:500 7.6px/9.5px "Roboto",sans-serif}
.sky-loc b{font-weight:700}
.sky-arrow{color:var(--teal-deep)}
.sky-map{position:absolute;left:0;top:404px;width:96px;height:76px;background:linear-gradient(135deg,#f4f6f7,#e2eef2 50%,#7fd8e6 75%,#f4f6f7)}

/* banner 468 */
.bnr{left:329px;top:222px;width:374px;height:48px}
.bnr .photo{width:122px;height:48px;clip-path:path("M0 0 H112 Q124 24 112 48 H0 Z")}
.bnr-arc{position:absolute;left:0;top:0;width:126px;height:48px}
.bnr-head{position:absolute;left:129px;top:4px;font:700 11px/14px "Montserrat",sans-serif}
.bnr-rule{position:absolute;left:129px;top:33px;width:120px;border-top:1px solid var(--sky)}
.bnr-voucher{position:absolute;left:129px;top:36px;font:500 7px/9px "Roboto",sans-serif}
.star{color:#f2c230}
.bnr-date{position:absolute;left:271px;top:6px;width:39px;height:22px;border:1px solid var(--navy);color:var(--teal);font:700 6px/8px "Montserrat",sans-serif;padding:2px 0 0 4px}
.bnr .logo{left:322px;top:2px;width:46px;height:44px}
.bnr .logo-dot{width:14px;height:14px}
.bnr .logo-name{font-size:5px}

/* leaderboard 728 */
.lead{left:329px;top:298px;width:582px;height:72px}
.lead .photo{width:192px;height:72px;clip-path:path("M0 0 H176 Q196 36 176 72 H0 Z")}
.lead-arc{position:absolute;left:0;top:0;width:196px;height:72px}
.lead-head{position:absolute;left:215px;top:18px;font:700 14px/17.5px "Montserrat",sans-serif;letter-spacing:.3px}
.lead-rule{position:absolute;left:215px;top:54px;width:175px;border-top:1px solid var(--sky)}
.lead-date{position:absolute;left:402px;top:15px;width:80px;height:44px;border:1px solid var(--navy);color:var(--teal);font:700 14px/17px "Montserrat",sans-serif;padding:4px 0 0 7px}
.lead .logo{left:505px;top:6px;width:68px;height:60px}
.lead .logo-dot{width:24px;height:24px}
.lead .logo-name{font-size:8px}

/* rectangles */
.rect{font-family:"Roboto",sans-serif}
.rect .photo{width:100%;height:62%}
.rect .wave{top:36%;height:27%}
.date-badge,.voucher-badge{position:absolute;background:var(--white);border:2px solid var(--sky);border-radius:50%}
.date-badge{width:64px;height:64px;right:-6px;top:-25px}
.date-text{position:absolute;right:5px;top:7px;font:500 7.6px/9px "Roboto",sans-serif;text-align:left;white-space:nowrap}
.voucher-badge{width:68px;height:68px;left:-14px;top:-19px}
.voucher-text{position:absolute;left:26px;top:22px;transform:translate(-50%,-50%) rotate(-28deg);font:500 7px/8.2px "Roboto",sans-serif;text-align:center;white-space:nowrap}
.rect-head{position:absolute;left:2%;top:65%;font:700 1.8em/1.1em "Roboto",sans-serif;white-space:nowrap}
.rect-sub{position:absolute;left:2%;top:73%;font:500 1.2em/1.2em "Roboto",sans-serif;color:var(--teal);white-space:nowrap}
.rect-rule{position:absolute;left:2%;top:81.5%;width:58%;border-top:1px solid var(--teal)}
.rect-rule::after{content:"";position:absolute;left:46%;top:-2px;width:9%;border-top:2px solid var(--teal)}
.rect-loc{position:absolute;left:2%;top:85%;font:700 .9em/1em "Roboto",sans-serif;white-space:nowrap}
.rect-loc span{color:var(--teal);font-weight:500}
.rect-bar{position:absolute;left:0;bottom:0;width:100%;height:5%;background:var(--teal);color:var(--white);font:500 .78em/1em "Roboto",sans-serif;display:flex;align-items:center;justify-content:center;white-space:nowrap}
.rect .logo{right:2%;top:63%;width:27%;height:25%}
.rect .logo-dot{width:2.6em;height:2.6em}
.rect .logo-name{font-size:.85em}

.r200{left:329px;top:425px;width:160px;height:160px;font-size:5.4px}
.r200 .photo{height:64%}
.r200 .rect-head{top:69%;font-size:1.95em}
.r200 .rect-sub{top:76.5%;font-size:1.45em}
.r200 .rect-rule{top:83%;width:62%}
.r200 .rect-loc{top:86%;font-size:1.05em}
.r200 .rect-bar{height:8%;font-size:1.55em;justify-content:flex-start;padding-left:3%}
.r200 .logo{top:67%;height:20%}
.r200 .date-badge{width:64px;height:64px;right:-14px;top:-26px}
.r200 .date-text{right:4px;top:6px;font-size:7.4px;line-height:8.8px}
.r250{left:538px;top:425px;width:200px;height:200px;font-size:8px}
.r300{left:791px;top:425px;width:240px;height:200px;font-size:8px}
.r336{left:187px;top:727px;width:269px;height:224px;font-size:9px}
.r336 .rect-sub{font-weight:400}
.r336 .date-badge{width:76px;height:76px;right:-22px;top:-29px}
.r336 .date-text{right:7px;top:11px;font-size:8px;line-height:9.6px}
.r336 .voucher-badge{width:80px;height:80px;left:-13px;top:-27px}
.r336 .voucher-text{left:32px;top:25px;font-size:8.6px;line-height:10px}
</style>
</head>
<body>
<div class="board">

  <!-- Skyscraper 120 x 600 -->
  <div class="size-label" style="left:232px;top:155px">120 X 600</div>
  <div class="ad sky">
    <div class="photo sunset" role="img" aria-label="Motor yacht cruising at sunset with a wake"></div>
    <svg class="wave" viewBox="0 0 100 100" preserveAspectRatio="none" aria-hidden="true">
      <path d="M0 60 Q50 10 100 30 L100 100 L0 100Z" fill="var(--white)"/>
      <path d="M0 55 Q50 5 100 25 L100 34 Q50 14 0 64Z" fill="var(--teal)"/>
    </svg>
    <div class="logo"><span class="logo-dot"></span><span class="logo-name">TIDE &amp; TALLY</span></div>
    <div class="sky-date">APRIL 29<br>MAY 1ST</div>
    <div class="sky-head"><span class="t">TIDE</span> AND<br>TALLY<br>DOCKSIDE<br><span class="t">BOAT FAIR</span></div>
    <div class="sky-rule"></div>
    <div class="sky-voucher">GET A<br>CHANCE WIN<br>A TROPICAL<br>TRAVEL VOUCHER</div>
    <div class="sky-loc"><span class="sky-arrow">&#10140;</span> <b>Location:</b> <span class="sky-arrow">&#11013;</span><br><span class="t">Grand Lake, Oklahoma</span></div>
    <div class="sky-map" role="img" aria-label="Map of Grand Lake showing the five dealer locations"></div>
  </div>

  <!-- Banner 468 x 60 -->
  <div class="ad bnr">
    <div class="photo sea" role="img" aria-label="White yacht speeding across dark blue water"></div>
    <svg class="bnr-arc" viewBox="0 0 126 48" aria-hidden="true"><path d="M112 0 Q124 24 112 48" fill="none" stroke="var(--teal)" stroke-width="3"/></svg>
    <div class="bnr-head"><span class="t">TIDE</span> AND TALLY<br>DOCKSIDE <span class="t">BOAT FAIR</span></div>
    <div class="bnr-rule"></div>
    <div class="bnr-voucher"><span class="star">&#9733;</span> Chance win a tropical&nbsp; travel voucher <span class="star">&#9733;</span></div>
    <div class="bnr-date">APRIL 29<br>MAY 1ST</div>
    <div class="logo"><span class="logo-dot"></span><span class="logo-name">TIDE &amp; TALLY</span></div>
  </div>
  <div class="size-label" style="left:752px;top:245px">468 X 60</div>

  <!-- Leaderboard 728 x 90 -->
  <div class="ad lead">
    <div class="photo sea" role="img" aria-label="Speedboat carving a white wake through open water"></div>
    <svg class="lead-arc" viewBox="0 0 196 72" aria-hidden="true"><path d="M176 0 Q196 36 176 72" fill="none" stroke="var(--teal)" stroke-width="4"/></svg>
    <div class="lead-head"><span class="t">TIDE</span> AND TALLY<br>DOCKSIDE <span class="t">BOAT FAIR</span></div>
    <div class="lead-rule"></div>
    <div class="lead-date">APRIL 29<br>MAY 1ST</div>
    <div class="logo"><span class="logo-dot"></span><span class="logo-name">TIDE &amp; TALLY</span></div>
  </div>
  <div class="size-label" style="left:970px;top:338px">728 X 90</div>

  <!-- Small Square 200 x 200 -->
  <div class="ad rect r200">
    <div class="photo lake" role="img" aria-label="Group of friends riding a white sport boat on a lake"></div>
    <svg class="wave" viewBox="0 0 100 100" preserveAspectRatio="none" aria-hidden="true">
      <path d="M0 45 Q45 105 100 40 L100 100 L0 100Z" fill="var(--white)"/>
      <path d="M0 30 Q45 100 100 30 L100 42 Q45 108 0 47Z" fill="var(--teal)"/>
      <path d="M60 68 Q85 60 100 44 L100 52 Q85 66 60 70Z" fill="var(--sky)"/>
    </svg>
    <div class="date-badge"></div>
    <div class="date-text">APRIL 29<br>MAY 1ST</div>
    <div class="rect-head">TIDE AND TALLY</div>
    <div class="rect-sub">DOCKSIDE BOAT FAIR</div>
    <div class="rect-rule"></div>
    <div class="rect-loc">LOCATION: <span>GRAND LAKE, OKLAHOMA</span></div>
    <div class="logo"><span class="logo-dot"></span><span class="logo-name">TIDE &amp; TALLY</span></div>
    <div class="rect-bar">Chance win a tropical travel voucher</div>
  </div>
  <div class="size-label" style="left:409px;top:614px">200 X 200</div>

  <!-- Square 250 x 250 -->
  <div class="ad rect r250">
    <div class="photo lake" role="img" aria-label="Group of friends riding a white sport boat on a lake"></div>
    <svg class="wave" viewBox="0 0 100 100" preserveAspectRatio="none" aria-hidden="true">
      <path d="M0 45 Q45 105 100 40 L100 100 L0 100Z" fill="var(--white)"/>
      <path d="M0 30 Q45 100 100 30 L100 42 Q45 108 0 47Z" fill="var(--teal)"/>
      <path d="M60 68 Q85 60 100 44 L100 52 Q85 66 60 70Z" fill="var(--sky)"/>
    </svg>
    <div class="voucher-badge"></div>
    <div class="voucher-text">Chance<br>win a tropical<br>travel voucher</div>
    <div class="date-badge"></div>
    <div class="date-text">APRIL 29<br>MAY 1ST</div>
    <div class="rect-head">TIDE AND TALLY</div>
    <div class="rect-sub">DOCKSIDE BOAT FAIR</div>
    <div class="rect-rule"></div>
    <div class="rect-loc">LOCATION: <span>GRAND LAKE, OKLAHOMA</span></div>
    <div class="logo"><span class="logo-dot"></span><span class="logo-name">TIDE &amp; TALLY</span></div>
    <div class="rect-bar">Over 100 new and pre-owned boats at 5 locations and 7 boat dealers</div>
  </div>
  <div class="size-label" style="left:637px;top:659px">250 X 250</div>

  <!-- Inline Rectangle 300 x 250 -->
  <div class="ad rect r300">
    <div class="photo lake" role="img" aria-label="Group of friends riding a white sport boat on a lake"></div>
    <svg class="wave" viewBox="0 0 100 100" preserveAspectRatio="none" aria-hidden="true">
      <path d="M0 45 Q45 105 100 40 L100 100 L0 100Z" fill="var(--white)"/>
      <path d="M0 30 Q45 100 100 30 L100 42 Q45 108 0 47Z" fill="var(--teal)"/>
      <path d="M60 68 Q85 60 100 44 L100 52 Q85 66 60 70Z" fill="var(--sky)"/>
    </svg>
    <div class="voucher-badge"></div>
    <div class="voucher-text">Chance<br>win a tropical<br>travel voucher</div>
    <div class="date-badge"></div>
    <div class="date-text">APRIL 29<br>MAY 1ST</div>
    <div class="rect-head">TIDE AND TALLY</div>
    <div class="rect-sub">DOCKSIDE BOAT FAIR</div>
    <div class="rect-rule"></div>
    <div class="rect-loc">LOCATION: <span>GRAND LAKE, OKLAHOMA</span></div>
    <div class="logo"><span class="logo-dot"></span><span class="logo-name">TIDE &amp; TALLY</span></div>
    <div class="rect-bar">Over 100 new and pre-owned boats at 5 locations and 7 boat dealers</div>
  </div>
  <div class="size-label" style="left:912px;top:654px">300 X 250</div>

  <!-- Large Rectangle 336 x 280 -->
  <div class="ad rect r336">
    <div class="photo lake" role="img" aria-label="Group of friends riding a white sport boat on a lake"></div>
    <svg class="wave" viewBox="0 0 100 100" preserveAspectRatio="none" aria-hidden="true">
      <path d="M0 45 Q45 105 100 40 L100 100 L0 100Z" fill="var(--white)"/>
      <path d="M0 30 Q45 100 100 30 L100 42 Q45 108 0 47Z" fill="var(--teal)"/>
      <path d="M60 68 Q85 60 100 44 L100 52 Q85 66 60 70Z" fill="var(--sky)"/>
    </svg>
    <div class="voucher-badge"></div>
    <div class="voucher-text">Chance<br>win a tropical<br>travel voucher</div>
    <div class="date-badge"></div>
    <div class="date-text">APRIL 29<br>MAY 1ST</div>
    <div class="rect-head">TIDE AND TALLY</div>
    <div class="rect-sub">DOCKSIDE BOAT FAIR</div>
    <div class="rect-rule"></div>
    <div class="rect-loc">LOCATION: <span>GRAND LAKE, OKLAHOMA</span></div>
    <div class="logo"><span class="logo-dot"></span><span class="logo-name">TIDE &amp; TALLY</span></div>
    <div class="rect-bar">Over 100 new and pre-owned boats at 5 locations and 7 boat dealers</div>
  </div>
  <div class="size-label" style="left:310px;top:995px">336 X 280</div>

</div>
</body>
</html>
```